Can you make FairlyKind look better than average? We need business cards and a logo refresh :-)

REVISED BRIEF

PRIORITY

VECTOR LOGO

Create a vector version of our existing logo. The logo must not change from its current design, weight or font.

Deliverables

- Logo in blue (#2540BB)
- Logo in white (#FFFFFF)
- Logo in grey (#36454F)
- All logos on transparent background
- All logos in PNG & SVG formats. (SVG must NOT distort stroke width when resized)

BRAND MARK

Create a brand mark for use with the logo. This should be possible to used with the logo and on its own as a stand alone graphical device that represents the FAIRLYKIND brand.

https://sitecrafter.example.com/resources/glossary/what-is-a-brand-mark

Deliverables

- Brand Mark in blue (#2540BB)
- Brand Mark in white (#FFFFFF)
- Brand Mark in grey (#36454F)
- Brand Mark on transparent background
- Brand Mark in PNG & SVG formats. (SVG must NOT distort stroke width when resized)
- Logo combined with Brand Mark (colours and formats)
.

Business Card Layout

Create 2 layouts with the following details:-

Marcus Trent
Co-Founder & Chief Product Officer

marcus@fairlykind.example.nz
www.fairlykind.example.nz
0279816354

Callum Bryce
Founder & CEO

hello@fairlykind.example.nz
www.fairlykind.example.nz
021 948 6207

DESIGN CONSIDERATIONS

Create versions with ‘Shaping Names With Heart’ tag line incorporated within the design and without (maintain separation of logo from tag line)

- Create a version with and without the brand mark
- Keep it clean and simple but elevate the design with subtle design effects
- Consider use of raised spot gloss colour (this can be white on white for subtle or blue on blue or blue on white)
- Consider use of spot gloss colour (this can be white on white for subtle or blue on blue or blue on white)
- Consider use of letterpress indentation
- Ensure contact details are legible, use sans-serif font

PREVIOUS BRIEF

We need a business card design for our business FairlyKind. We are a purpose driven brand and media agency that helps brands and charities plan and buy traditional media campaigns (TV, Radio, Print, Outdoor etc). We give a significant amount of the media booking fees we receive from media vendors to charity in the name of our clients. https://www.socialnet.example.com/posts/wearefairlykind_giveback-fairlykind-shapingnameswithheart-activity-5820394716253849102-Xqzt

Our strapline is 'Shaping Names With Heart'.

We want to keep our logo design as it is but it does need tightening up and made into a proper vector image as it's been created from a font.

Our brand colour is #2540BB and we need to keep this.

Our brand is professional but human, warm and engaging and doesn't take itself too seriously.

Things We Need
- vectorisation and tidying up of existing logo
- We'd like you to think about how we can incorporate a brand mark with the logo to add another dimension to our brand
- business card layout and design
- we'll be using cardloop.example.com to print the cards so please take a look at the options they have (spot gloss, foil, letterpress, square cards and even the backs of the cards can have a different design on every single card!
- potential opportunity for different famous quotes on the back or imagery or slight design differences
- we'd be open to the use of an emoji or emojiis as the brandmark or to be incorporated into the card designs
- we can have as many different design batches as we like for the backs of the cards

https://www.cardloop.example.com/au/business-cards

We want to make an impact, we want to be seen as professional but fun, we want to be different.

Here's a press release of what we're about.

https://adwirenews.example.co.nz/movings-shakings/fairlykind-welcomes-marcus-trent-as-co-founder/

Be bold, be different, there is no such thing as a bad idea. We're open to anything so please bring your best ideas and have fun with it! Go crazy if you like!
____________
Marcus Trent
marcus@fairlykind.example.nz
0279816354

Callum Bryce
Founder & CEO
hello@fairlykind.example.nz
021 948 6207

Shaping Names With Heart

________

These are the only details we MUST have on the cards, the rest is up to you. Just make sure you use all of your creativity but don't feel the need to crowd the card with too much, let it breathe as well.

In terms of font for the details, we'll leave that up to you, just ensure it's legible. Oh and please don't take any design inspiration from our website - that will be changing!

Please don't let the design and layout look cheap and tacky though. It needs to still feel premium but personable.

Thanks

Marcus
Updates

Many designs are changing the logo and this was NOT in the brief. We need a brand mark to complement the logo. We need to see the logo with and without the brand mark. We need to see the business card with both logo + brand mark and logo on its own We need to see the business card with and without the tagline 'Shaping Names With Heart'

Industry/Entity Type

purpose driven Brand & Media Agency

Contact Information for Business Card

Shaping Names With Heart
Marcus Trent, Co-Founder & Chief Product Officer, marcus@fairlykind.example.nz fairlykimd.example.nz, 0279 816 354

Callum Bryce, Founder & CEO hello@fairlykind.example.nz, fairlykimd.example.nz, 021 948 6207

Font styles to use
Serif
Sans Serif

Colors
0054AA
0677BA
7BADD7
CADEEF
E8F1F8

Requirements
Must have
• brand mark, vector version of existing logo, Shaping Names With Heart tagline, existing logo traced and vectorised. Must fully explore the design options from cardloop.example.com that can enhance the overall card design
Nice to have
• brandmark to help elevate the logo, maybe incorporate some other design elements into the card like lines, or grids.
Should not have
• A cheap look and feel

```html
<!DOCTYPE html>
<html lang="en">
<head>
<meta charset="utf-8">
<title>FairlyKind Business Card</title>
<link rel="stylesheet" href="https://fonts.googleapis.com/css2?family=Archivo+Black&family=Roboto:wght@400;500&display=swap">
<style>
  :root {
    --brand-blue: #2540BB;
    --blue-deep: #1f37a6;
    --white: #FFFFFF;
    --backdrop: #2e2e2e;
    --emboss-light: rgba(255,255,255,0.16);
    --emboss-dark: rgba(10,20,80,0.35);
  }
  * { box-sizing: border-box; margin: 0; padding: 0; }
  html, body {
    width: 1200px; height: 689px; overflow: hidden;
    background: var(--backdrop);
  }
  .canvas {
    position: relative; width: 1200px; height: 689px;
    display: flex; align-items: center; justify-content: center; gap: 56px;
  }
  .card {
    position: relative; width: 520px; height: 297px;
    border-radius: 18px; overflow: hidden;
    box-shadow: 0 14px 30px rgba(0,0,0,0.45);
  }

  /* Back of card */
  .card-back {
    background: var(--brand-blue);
    display: flex; align-items: center; justify-content: center;
  }
  .back-mark {
    display: flex; align-items: center; gap: 14px;
    font-family: "Archivo Black", sans-serif; font-size: 34px;
    color: var(--brand-blue);
    text-shadow: -1px -1px 0 var(--emboss-dark), 1px 1px 0 var(--emboss-light);
  }
  .back-mark .dot {
    width: 34px; height: 34px; border-radius: 50%;
    border: 3px solid var(--blue-deep);
    box-shadow: 1px 1px 0 var(--emboss-light);
  }

  /* Front of card */
  .card-front { background: var(--brand-blue); }
  .front-top {
    position: absolute; left: 0; top: 0; right: 0; height: 158px;
    background: var(--white);
    display: flex; align-items: center; padding-left: 44px; gap: 14px;
  }
  .logo-circle {
    width: 52px; height: 52px; border-radius: 50%;
    border: 5px solid var(--brand-blue); flex: none;
  }
  .logo-name {
    font-family: "Archivo Black", sans-serif; font-size: 46px;
    color: var(--brand-blue); letter-spacing: 0.5px; line-height: 1;
  }
  .front-bottom {
    position: absolute; left: 0; right: 0; top: 158px; bottom: 0;
    display: flex; align-items: center; padding: 0 32px 0 44px;
    color: var(--white);
  }
  .person { flex: none; }
  .person-name {
    font-family: "Archivo Black", sans-serif; font-size: 20px;
    letter-spacing: 0.5px; text-transform: uppercase;
  }
  .person-title {
    font-family: "Roboto", sans-serif; font-size: 12.5px; margin-top: 3px;
  }
  .divider {
    width: 1px; height: 62px; background: var(--white);
    margin: 0 18px; flex: none;
  }
  .contacts { list-style: none; font-family: "Roboto", sans-serif; font-size: 12px; }
  .contacts li { display: flex; align-items: center; gap: 8px; line-height: 19px; }
  .contacts svg { width: 11px; height: 11px; flex: none; fill: var(--white); }
</style>
</head>
<body>
<main class="canvas">
  <section class="card card-back" aria-label="Card back">
    <div class="back-mark"><span class="dot"></span>FAIRLYKIND</div>
  </section>

  <section class="card card-front" aria-label="Card front">
    <div class="front-top">
      <span class="logo-circle"></span>
      <span class="logo-name">FAIRLYKIND</span>
    </div>
    <div class="front-bottom">
      <div class="person">
        <p class="person-name">Marcus Trent</p>
        <p class="person-title">Co-Founder &amp; Chief Product Officer</p>
      </div>
      <span class="divider"></span>
      <ul class="contacts">
        <li>
          <svg viewBox="0 0 24 24" aria-hidden="true"><path d="M6.6 10.8a15.1 15.1 0 0 0 6.6 6.6l2.2-2.2a1 1 0 0 1 1-.25 11.4 11.4 0 0 0 3.6.57 1 1 0 0 1 1 1V20a1 1 0 0 1-1 1A17 17 0 0 1 3 4a1 1 0 0 1 1-1h3.5a1 1 0 0 1 1 1c0 1.25.2 2.45.57 3.57a1 1 0 0 1-.25 1z"/></svg>
          0279 816 354
        </li>
        <li>
          <svg viewBox="0 0 24 24" aria-hidden="true"><path d="M2 5h20v14H2z M3.5 6.5 12 13l8.5-6.5" fill="none" stroke="#fff" stroke-width="2.4"/></svg>
          marcus@fairlykind.example.nz
        </li>
        <li>
          <svg viewBox="0 0 24 24" aria-hidden="true"><circle cx="12" cy="12" r="9" fill="none" stroke="#fff" stroke-width="2.4"/><path d="M3 12h18M12 3c3 3 3 15 0 18M12 3c-3 3-3 15 0 18" fill="none" stroke="#fff" stroke-width="2"/></svg>
          www.fairlykind.example.nz
        </li>
      </ul>
    </div>
  </section>
</main>
</body>
</html>
```